Bluecrest Automotive Service Website Design

We are working with Bluecrest Automotive Service. They are a local mechanic/garage and in need of a new website design.

Some sites to use for inspiration:

https://www.torvalcar.example
https://www.quenbo.example
https://pavels-carcare.example
https://www.ashgrovetotalautocare.example/

Thank you for taking the time to consider designing a website for us. We are web developers based in Stockton, CA, USA. Most of our projects go through the same process. Understanding this process may help you win a project with us. We custom-code all of our websites in-house. We don’t have any requirements as to what tools you use for your design, but we prefer Figma files. For any design that we label as four-stars, we send it to the client for review. The client picks the final design they want us to use. Once we complete this process, we will continue to show additional clients all the four-star sites and purchase them later. Your designs will have multiple chances to sell. For better chances of success, we ask that you follow these guidelines.

IMAGES:
If you use any images or icons in the design, we ask that you have a link to the asset so we can purchase the image/icon. Most of the designs we submit do not have the customer’s images on them unless they have some great images. Be creative; show us the feeling you are trying to portray with your image choices. Use any royalty-free site you choose. We subscribe to Adobe and mainly use their images, but we can purchase images outside of Adobe.

PLEASE NOTE: we will not submit designs to clients with watermarks on the images.

FONTS:
We ask that you identify the fonts used in the design. This can be done in a message if you want. We typically use Google Fonts and Adobe Fonts.

CONTENT:
We're always open to different content and ideas. We often submit designs with stock images so the client can see our vision. We typically take pictures after the website launch to use their images with our vision. Lorem Ipsum is fine for paragraphs, but we ask that you write the headers in correct English. We want to be able to show the vision and identify the sections of the website.

INSPIRATION:
We typically add a couple of links in the brief of websites we like to help you get started in your design.

REVISIONS:
We do not often ask for revisions of the designs unless we see something in the design that may not appeal to the client. If there are slight changes that we want to make, we do that in the development process.

FEEDBACK:
We rarely give feedback on designs during the design process. We are working on many website projects and do not have the time to provide feedback. We usually respond if your request is well thought out and asks specific questions, but a note asking “feedback, please” usually goes unanswered.

```html
<!DOCTYPE html>
<html lang="en">
<head>
<meta charset="utf-8">
<title>Bluecrest Automotive Service</title>
<link rel="stylesheet" href="https://fonts.googleapis.com/css2?family=Bebas+Neue&family=Roboto+Condensed:wght@400;500;700&family=Roboto:wght@700&display=swap">
<style>
:root{
  --red:#b00f0f;
  --red-dark:#8e0b0b;
  --gray:#9d9d9d;
  --gray-light:#a7a7a7;
  --ink:#1e1e1e;
  --text:#5c5c5c;
  --white:#ffffff;
  --footer:#8d8d8d;
}
*{box-sizing:border-box;margin:0;padding:0}
html,body{width:1200px;height:3333px;overflow:hidden;background:var(--white)}
body{position:relative;font-family:"Roboto Condensed",Arial,sans-serif;color:var(--ink)}
.abs{position:absolute}
.display{font-family:"Bebas Neue",Impact,sans-serif;font-weight:400;line-height:1;letter-spacing:.5px}
.btn{position:absolute;display:flex;align-items:center;justify-content:center;height:44px;width:208px;font-family:"Roboto Condensed",sans-serif;font-weight:700;font-size:15px;color:var(--white);text-transform:uppercase;text-decoration:none}
.btn--red{background:var(--red)}
.btn--gray{background:var(--gray-light)}
.btn--outline{border:1px solid var(--white)}

.topbar{left:0;top:0;width:1200px;height:40px;background:var(--red)}
.topbar__hours{left:568px;top:0;height:40px;display:flex;align-items:center;gap:9px;color:var(--white);font-weight:700;font-size:15px}
.topbar__cta{left:812px;top:0;width:243px;height:40px;background:var(--gray-light);color:var(--white);font-weight:700;font-size:15px;display:flex;align-items:center;justify-content:center}
.brandbox{left:144px;top:0;width:249px;height:114px;background:var(--white);box-shadow:0 4px 14px rgba(0,0,0,.12);display:flex;align-items:center;justify-content:center}
.brandbox .display{font-size:56px;color:var(--gray)}
.nav{left:433px;top:70px;width:622px;display:flex;justify-content:space-between;font-size:15px;font-weight:500}
.nav a{color:var(--ink);text-decoration:none}
.nav .active{border-left:2px solid var(--red);padding-left:7px}

.hero{left:0;top:114px;width:1200px;height:549px;background:linear-gradient(90deg,#7a7a7a 0%,#3b4052 35%,#1d1d1f 60%,#0f0f10 100%)}
.hero__title{left:624px;top:214px;font-size:58px;color:var(--white);line-height:64px}
.hero__title .red{color:var(--red)}
.hero__dots{left:1131px;top:350px}
.hero__dots span{display:block;width:6px;height:6px;border-radius:50%;background:var(--white);margin-bottom:10px}
.hero__dots span.on{background:var(--red)}

.locator{left:144px;top:602px;width:911px;height:120px;background:var(--white);box-shadow:0 10px 30px rgba(0,0,0,.12)}
.locator__title{left:71px;top:40px;font-size:46px;color:var(--gray)}
.locator__title .red{color:var(--red)}
.locator__input{left:398px;top:38px;width:304px;height:46px;border:1px solid #cfcfcf;display:flex;align-items:center;padding-left:20px;gap:8px;font-size:13px;color:#444}
.locator__btn{left:711px;top:39px;width:128px;height:44px;background:var(--red);color:var(--white);font-weight:700;font-size:16px;display:flex;align-items:center;justify-content:center;gap:10px}

.welcome__kicker{left:0;top:826px;width:1200px;text-align:center;font-size:58px;color:var(--gray)}
.welcome__title{left:0;top:893px;width:1200px;text-align:center;font-size:50px;color:var(--red)}
.welcome__text{left:221px;top:980px;width:758px;font-size:16px;line-height:30px;color:var(--text);text-align:justify;text-align-last:center}

.services__photo{left:47px;top:1300px;width:486px;height:558px;background:radial-gradient(circle at 60% 40%,#8a6a2a 0%,#3a3d44 35%,#1c1f26 100%)}
.services__frame{left:533px;top:1371px;width:262px;height:100px;border:3px solid var(--red);border-left:none;border-bottom:none}
.services__card{left:468px;top:1431px;width:583px;height:558px;background:var(--white);box-shadow:0 10px 40px rgba(0,0,0,.12)}
.services__kicker{left:56px;top:88px;font-size:48px;color:var(--gray)}
.services__title{left:56px;top:148px;font-size:48px;color:var(--red)}
.service{position:absolute;display:flex;align-items:center;gap:16px;font-family:Roboto,Arial,sans-serif;font-weight:700;font-size:16px;line-height:22px;letter-spacing:.3px;text-transform:uppercase;color:var(--ink)}
.service__icon{width:70px;height:70px;border-radius:50%;border:2px solid #ddd;display:flex;align-items:center;justify-content:center;flex:none;background:var(--white)}
.service__icon--on{background:var(--red);border-color:#e3b0b0}

.why__title{left:144px;top:2094px;font-size:50px;color:var(--gray)}
.why__title .red{color:var(--red)}
.why__text{left:144px;top:2169px;width:455px;font-size:16px;line-height:30px;color:var(--text);text-align:justify}
.why__frame{left:875px;top:2353px;width:228px;height:203px;border:3px solid var(--red)}
.why__photo{left:667px;top:2074px;width:388px;height:430px;background:linear-gradient(160deg,#bfc6cf 0%,#6f7783 45%,#2b2f36 100%)}

.cta{left:0;top:2599px;width:1200px;height:326px;background:linear-gradient(90deg,var(--red) 0%,#c0151a 50%,var(--red-dark) 100%)}
.cta__title{left:0;top:92px;width:1200px;text-align:center;font-size:50px;color:var(--white)}

.footer{left:0;top:2925px;width:1200px;height:408px;background:var(--footer);color:var(--white)}
.footer__brand{left:144px;top:70px;font-size:82px;color:var(--white)}
.footer__addr{left:144px;top:192px;display:flex;gap:13px;font-size:16px;line-height:24px}
.footer__phone{left:144px;top:252px;display:flex;align-items:center;gap:13px;font-size:20px;font-weight:500}
.footer__rule{top:46px;width:1px;height:238px;background:rgba(255,255,255,.35)}
.footer__head{font-size:30px;color:var(--white)}
.footer__links{font-size:16px;line-height:31px}
.footer__links a{display:block;color:var(--white);text-decoration:none}
.social{position:absolute;top:195px;width:38px;height:38px;border-radius:50%;background:var(--white);border:2px solid #d9d9d9}
.footer__legal{left:0;top:339px;width:1200px;text-align:center;font-size:16px}
</style>
</head>
<body>

<header>
  <div class="abs topbar"></div>
  <div class="abs topbar__hours">
    <svg width="20" height="20" viewBox="0 0 20 20" aria-hidden="true"><circle cx="10" cy="10" r="9" fill="#fff"/><path d="M10 5v5l3 2" stroke="#b00f0f" stroke-width="2" fill="none"/></svg>
    Mon - Fri: 8:00 AM - 5:30 PM
  </div>
  <div class="abs topbar__cta">MAKE AN APPOINTMENT</div>
  <div class="abs brandbox"><span class="display">BLUECREST</span></div>
  <nav class="abs nav">
    <a class="active" href="#">HOME</a><a href="#">ABOUT</a><a href="#">SERVICES</a><a href="#">VEHICLES</a><a href="#">SPECIALS</a><a href="#">REVIEWS</a><a href="#">DIRECTIONS</a>
  </nav>
</header>

<section>
  <div class="abs hero" role="img" aria-label="Smiling mechanic in a blue work jacket leaning over a car engine in a garage"></div>
  <h1 class="abs display hero__title">RELIABLE REPAIRS.<br><span class="red">HONEST SERVICE.</span><br>EVERY TIME.</h1>
  <a class="btn btn--red" style="left:626px;top:437px">Request a Quote</a>
  <a class="btn btn--gray" style="left:847px;top:437px">Get Started</a>
  <div class="abs hero__dots"><span></span><span class="on"></span><span></span></div>

  <div class="abs locator">
    <h2 class="abs display locator__title">FIND A <span class="red">LOCATION</span></h2>
    <div class="abs locator__input">
      <svg width="9" height="12" viewBox="0 0 9 12" aria-hidden="true"><path d="M4.5 0A4.5 4.5 0 0 0 0 4.5C0 8 4.5 12 4.5 12S9 8 9 4.5A4.5 4.5 0 0 0 4.5 0z" fill="#999"/><circle cx="4.5" cy="4.5" r="1.7" fill="#fff"/></svg>
      Enter Zipcode
    </div>
    <div class="abs locator__btn">
      <svg width="16" height="16" viewBox="0 0 16 16" aria-hidden="true"><circle cx="6.5" cy="6.5" r="5" stroke="#fff" stroke-width="2.4" fill="none"/><path d="M10.5 10.5L15 15" stroke="#fff" stroke-width="2.6"/></svg>
      SEARCH
    </div>
  </div>
</section>

<section>
  <h2 class="abs display welcome__kicker">WELCOME TO</h2>
  <h2 class="abs display welcome__title">BLUECREST AUTOMOTIVE SERVICE</h2>
  <p class="abs welcome__text">Sed ut perspiciatis unde omnis iste natus error sit voluptatem accusantium doloremque laudantium, totam rem aperiam, eaque ipsa quae ab illo inventore veritatis et quasi architecto beatae vitae dicta sunt explicabo. Nemo enim ipsam voluptatem quia voluptas sit aspernatur aut odit aut fugit, sed quia consequuntur magni dolores eos qui ratione voluptatem sequi nesciunt. Neque porro quisquam est, qui dolorem ipsum quia dolor sit amet, consectetur, adipisci ven numquam eius modi tempobore et dolore magnam aliquam quaerat voluptatem.</p>
  <a class="btn btn--red" style="left:385px;top:1166px">Read More</a>
  <a class="btn btn--gray" style="left:606px;top:1166px">Request a Quote</a>
</section>

<section>
  <div class="abs services__frame"></div>
  <div class="abs services__photo" role="img" aria-label="Motor oil being poured into a car engine"></div>
  <div class="abs services__card">
    <h2 class="abs display services__kicker">TIRES, OIL CHANGES AND</h2>
    <h2 class="abs display services__title">AUTO REPAIR SERVICES</h2>

    <div class="service" style="left:53px;top:223px">
      <span class="service__icon"><svg width="40" height="40" viewBox="0 0 40 40" aria-hidden="true"><circle cx="17" cy="22" r="9" stroke="#b00f0f" stroke-width="2" fill="none"/><circle cx="17" cy="22" r="3.5" stroke="#b00f0f" stroke-width="2" fill="none"/><path d="M27 12l8-4M28 18h7M27 24l7 3" stroke="#b00f0f" stroke-width="2"/></svg></span>OIL CHANGE</div>
    <div class="service" style="left:291px;top:223px">
      <span class="service__icon"><svg width="40" height="40" viewBox="0 0 40 40" aria-hidden="true"><circle cx="20" cy="20" r="14" stroke="#b00f0f" stroke-width="2" fill="none"/><circle cx="20" cy="20" r="7" stroke="#b00f0f" stroke-width="2" fill="none"/><circle cx="20" cy="20" r="2" fill="#b00f0f"/></svg></span>BRAKES &amp;<br>BRAKE REPAIR</div>
    <div class="service" style="left:53px;top:312px">
      <span class="service__icon service__icon--on"><svg width="40" height="40" viewBox="0 0 40 40" aria-hidden="true"><rect x="7" y="12" width="24" height="20" rx="2" stroke="#fff" stroke-width="2" fill="none"/><circle cx="29" cy="28" r="6" stroke="#fff" stroke-width="2" fill="#b00f0f"/><path d="M14 12V8h10v4" stroke="#fff" stroke-width="2" fill="none"/></svg></span>TIRE<br>MAINTENANCE</div>
    <div class="service" style="left:291px;top:312px">
      <span class="service__icon"><svg width="40" height="40" viewBox="0 0 40 40" aria-hidden="true"><circle cx="20" cy="18" r="11" stroke="#b00f0f" stroke-width="2" fill="none"/><circle cx="20" cy="18" r="4" stroke="#b00f0f" stroke-width="2" fill="none"/><path d="M9 33h22" stroke="#b00f0f" stroke-width="2"/></svg></span>SHOP FOR TIRES</div>
    <div class="service" style="left:53px;top:399px">
      <span class="service__icon"><svg width="40" height="40" viewBox="0 0 40 40" aria-hidden="true"><circle cx="20" cy="20" r="14" stroke="#b00f0f" stroke-width="2" fill="none"/><circle cx="20" cy="20" r="4" stroke="#b00f0f" stroke-width="2" fill="none"/><path d="M7 18h9M24 18h9M20 24v10" stroke="#b00f0f" stroke-width="2"/></svg></span>STEERING &amp;<br>SUSPENSION</div>
    <div class="service" style="left:291px;top:399px">
      <span class="service__icon"><svg width="40" height="40" viewBox="0 0 40 40" aria-hidden="true"><path d="M6 26v-6l4-8h20l4 8v6z" stroke="#b00f0f" stroke-width="2" fill="none"/><circle cx="12" cy="21" r="2" fill="#b00f0f"/><circle cx="28" cy="21" r="2" fill="#b00f0f"/><path d="M8 26v4h5v-4M27 26v4h5v-4" stroke="#b00f0f" stroke-width="2" fill="none"/></svg></span>CAR A/C &amp; HEATING<br>REPAIR</div>
  </div>
</section>

<section>
  <h2 class="abs display why__title">WHY <span class="red">CHOOSE US</span></h2>
  <p class="abs why__text">Sed ut perspiciatis unde omnis iste natus error sit voluptatem accusantium doloremque laudantium, totam rem aperiam, eaque ipsa quae ab illo inventore veritatis et quasi architecto beatae vitae dicta sunt explicabo. Nemo enim ipsam voluptatem quia voluptas sit aspernatur aut odit aut fugit, sed quia consequuntur magni dolores eos qui ratione voluptatem sequi nesciunt. Neque porro quisquam est, qui dolorem ipsum quia dolor sit amet, consectetur, adipisci ven numquam eius modi tempobore et dolore magnam aliquam quaerat voluptatem.</p>
  <a class="btn btn--red" style="left:144px;top:2436px">Read More</a>
  <div class="abs why__frame"></div>
  <div class="abs why__photo" role="img" aria-label="Mechanic in white gloves rolling a car tire in a workshop"></div>
</section>

<section class="abs cta" aria-label="Schedule service">
  <div class="abs" style="inset:0" role="img" aria-label="Mechanic with arms crossed in a garage, tinted red"></div>
  <h2 class="abs display cta__title">SCHEDULE YOUR SERVICE TODAY</h2>
  <a class="btn btn--gray" style="left:384px;top:181px">Book Appointment</a>
  <a class="btn btn--outline" style="left:608px;top:181px">Contact Us</a>
</section>

<footer class="abs footer">
  <div class="abs display footer__brand">BLUECREST</div>
  <div class="abs footer__addr">
    <svg width="20" height="16" viewBox="0 0 20 16" style="margin-top:4px" aria-hidden="true"><path d="M0 2l6-2 8 2 6-2v14l-6 2-8-2-6 2z" fill="#fff"/><path d="M6 0v14M14 2v14" stroke="#8d8d8d" stroke-width="1.2"/></svg>
    <span>123,Sed ut perspiciatis unde omnis<br>iste natus error sit volupta</span>
  </div>
  <div class="abs footer__phone">
    <svg width="18" height="18" viewBox="0 0 18 18" aria-hidden="true"><path d="M3 1l3 0 2 4-2 2c1 2 3 4 5 5l2-2 4 2v3c0 1-1 2-2 2C8 17 1 10 1 3c0-1 1-2 2-2z" fill="#fff"/></svg>
    +1 555 014 2277
  </div>

  <div class="abs footer__rule" style="left:463px"></div>
  <div class="abs footer__rule" style="left:790px"></div>

  <h3 class="abs display footer__head" style="left:525px;top:68px">LINKS</h3>
  <div class="abs footer__links" style="left:527px;top:108px"><a>Home</a><a>Vehicles</a><a>Services</a><a>About Us</a><a>Specials</a></div>
  <div class="abs footer__links" style="left:647px;top:108px"><a>Reviews</a><a>Appointments</a><a>Directions</a></div>

  <h3 class="abs display footer__head" style="left:844px;top:68px">SOCIAL MEDIA</h3>
  <a class="btn btn--red" style="left:846px;top:119px">Book Appointment</a>
  <span class="social" style="left:845px" aria-label="Social profile"></span>
  <span class="social" style="left:893px" aria-label="Social profile"></span>
  <span class="social" style="left:940px" aria-label="Social profile"></span>
  <span class="social" style="left:988px" aria-label="Social profile"></span>

  <p class="abs footer__legal">© 2025 Companyname. All Rights Reserved &nbsp;|&nbsp; Privacy Policy &nbsp;|&nbsp; Terms of use</p>
</footer>

</body>
</html>
```